Front of folder with Vision/Mission/Culture design

To design a print template for front of folders, two front options

Must include the following:-

1) Logo
2)Vision
3) Mission

Or
1) Logo
2) Culture
3) Value

Our Vision
“To be the leading capability developer in the global fashion industry.”

Our Mission
“To inculcate in each individual the attitude, skills and knowledge which contribute to the development of the textile and fashion industry.”

Our Values
Lumo.vk is committed to delivering unique, professional training programmes, as well as providing a networking platform for students, professionals and the industry itself.
• UNIQUE
We offer unique and highly efficient industry-based training programmes that provide the most relevant skills, knowledge and attitude to compete in the global textile and fashion industry. Eligible participants enjoy KPR funding, internship opportunities, training allowances and industry visits.
• PROFESSIONAL
Our courses are based on industry practices and not just theory. That’s because we only recruit professional industry practitioners and experts – all of whom are passionate about sharing their expertise with the next generation through consulting, mentoring and training.
• NETWORK
An impressive global and local network of partnerships in the fashion and textile industry enables us to open doors to exciting careers. It also ensures that the Academy is continuously up-to-date with the latest developments in the global fashion world.

Our Culture
• COMMITMENT
We are committed to our vision and mission.
• OWNERSHIP
We take ownership in everything we do.
• RESPECT
We respect people, companies and utilization of resources.
• DIVERSITY
We embrace diversity in thoughts, culture, age, religion and sexuality.

Industry/Entity Type

Training

Requirements
Must have
• Compulsory on the front cover of the file/folder
Logo should be discrete. Vision Mission is the focus.

Logo
mission and vision statements

Corporate colours are red, black and grey.

```html
<!DOCTYPE html>
<html lang="en">
<head>
<meta charset="utf-8">
<title>Lumo.vk – Folder Front, Vision &amp; Mission</title>
<link rel="stylesheet" href="https://fonts.googleapis.com/css2?family=Cinzel:wght@600&family=Jost:wght@300;400;500&display=swap">
<style>
  :root {
    --page-bg: #e2e2e2;
    --folder-bg: #444446;
    --ink: #ffffff;
    --ghost: rgba(255, 255, 255, 0.26);
    --rule: #ffffff;
  }
  * { margin: 0; padding: 0; box-sizing: border-box; }
  html, body { width: 1072px; height: 1200px; overflow: hidden; background: var(--page-bg); }
  .folder-front {
    position: absolute; left: 70px; top: 139px;
    width: 934px; height: 986px;
    background: var(--folder-bg);
    color: var(--ink);
    font-family: "Jost", sans-serif;
    overflow: hidden;
  }
  .spine-rule {
    position: absolute; left: 220px; top: 0; bottom: 0;
    width: 1px; background: var(--rule);
  }
  .brand-name {
    position: absolute; left: 282px; top: 46px;
    font-family: "Jost", sans-serif; font-weight: 400;
    font-size: 34px; line-height: 1; letter-spacing: -0.5px; color: var(--ink);
  }
  .statement-block {
    position: absolute; left: 220px; width: 714px;
    text-align: center;
  }
  .statement-block .ghost-title {
    position: absolute; left: -40px; right: -40px;
    font-family: "Cinzel", serif; font-weight: 600;
    line-height: 1; color: var(--ghost);
    white-space: nowrap; text-align: center;
  }
  .statement-block .title {
    position: relative;
    font-family: "Cinzel", serif; font-weight: 600;
    font-size: 50px; line-height: 1; letter-spacing: 0;
    white-space: nowrap;
  }
  .statement-block .quote {
    position: relative;
    font-family: "Jost", sans-serif; font-weight: 400;
    font-size: 15.5px; line-height: 20px; text-transform: uppercase;
    letter-spacing: -0.2px;
  }
  .vision { top: 280px; }
  .vision .ghost-title { top: 20px; font-size: 100px; letter-spacing: -1px; }
  .vision .title { left: 14px; }
  .vision .quote { margin-top: 30px; left: 14px; }
  .mission { top: 534px; }
  .mission .ghost-title { top: 26px; font-size: 94px; letter-spacing: -3px; }
  .mission .title { left: 0; }
  .mission .quote { margin-top: 38px; left: 2px; }
  .contact-bar {
    position: absolute; top: 944px; left: 0; right: 0;
    font-family: "Jost", sans-serif; font-weight: 500; font-size: 13px;
    line-height: 15px;
  }
  .contact-item { position: absolute; display: flex; align-items: flex-start; gap: 6px; }
  .contact-item svg { flex: none; fill: var(--ink); }
  .contact-phone { left: 316px; top: 4px; }
  .contact-email { left: 461px; top: 2px; gap: 12px; }
  .contact-address { left: 667px; top: 0; gap: 14px; }
</style>
</head>
<body>
  <main class="folder-front">
    <div class="spine-rule"></div>

    <div class="brand-name">Lumo.vk</div>

    <section class="statement-block vision">
      <div class="ghost-title" aria-hidden="true">OUR VISION</div>
      <h2 class="title">OUR VISION</h2>
      <p class="quote">“To be the leading capability developer in the global fashion industry.”</p>
    </section>

    <section class="statement-block mission">
      <div class="ghost-title" aria-hidden="true">OUR MISSION</div>
      <h2 class="title">OUR MISSION</h2>
      <p class="quote">“To inculcate in each individual the attitude, skills and knowledge<br>which contribute to the development of the textile and fashion industry.”</p>
    </section>

    <footer class="contact-bar">
      <div class="contact-item contact-phone">
        <svg width="16" height="16" viewBox="0 0 24 24" aria-hidden="true"><path d="M6.6 10.8a15.1 15.1 0 0 0 6.6 6.6l2.2-2.2c.3-.3.7-.4 1-.2 1.1.4 2.3.6 3.6.6.6 0 1 .4 1 1V20c0 .6-.4 1-1 1A17 17 0 0 1 3 4c0-.6.4-1 1-1h3.5c.6 0 1 .4 1 1 0 1.3.2 2.5.6 3.6.1.3 0 .7-.2 1z"/></svg>
        <span>555-000-0009</span>
      </div>
      <div class="contact-item contact-email">
        <svg width="16" height="12" viewBox="0 0 16 12" aria-hidden="true"><path d="M0 0h16v12H0z" opacity=".85"/><path d="M0 0l8 6 8-6" fill="none" stroke="#444446" stroke-width="1.4"/></svg>
        <span>info@yourdomain.com</span>
      </div>
      <div class="contact-item contact-address">
        <svg width="18" height="16" viewBox="0 0 18 16" aria-hidden="true"><path d="M9 0l9 8h-2.5v8h-4.5v-5h-4v5H2.5V8H0z"/></svg>
        <span>000 N. Alder Road<br>Fern Park,Place 0009</span>
      </div>
    </footer>
  </main>
</body>
</html>
```